WEBSITE NEEDED FOR MY COMPANY CALLED BRAVERIDGE HOCKEY DEVELOPMENT

LOOKING FOR A WEBSITE TO MARKET AND SEEL MY HOCKEY DEVELOPMENT PROGRAMS.
NEEDS TO HAVE 5+ PAGES

Target Market(s)

YOUTH SPORTS

Industry/Entity Type

YOUTH ATHLETE DEVELOPMENT

Number of Pages Required

5+ page

Font styles to use
Sans Serif

Colors
0054AA
0677BA
7BADD7
CADEEF
E8F1F8

Requirements
Must have
• MAIN PAGE - SPIRNG PROGRAM PAGE - SUMMER PROGRAM PAGE - WINTER PAGE - TOURNAMENT PAGE
Nice to have
• FLASH
Should not have
• NOT SURE

```html
<!DOCTYPE html>
<html lang="en">
<head>
<meta charset="utf-8">
<title>Braveridge Hockey Development</title>
<link href="https://fonts.googleapis.com/css2?family=Poppins:wght@400;500;600;700&display=swap" rel="stylesheet">
<style>
:root{
  --navy:#1f2b3a;
  --ink:#243244;
  --cyan:#2bb4e6;
  --blue:#0677ba;
  --pale:#f4f5f7;
  --text:#8a919b;
  --white:#ffffff;
}
*{box-sizing:border-box;margin:0;padding:0}
html,body{width:1200px;height:3848px;overflow:hidden}
body{font-family:"Poppins",sans-serif;color:var(--ink);background:var(--white);position:relative}
a{color:inherit;text-decoration:none}
.btn{display:inline-block;border-radius:30px;font-size:13px;font-weight:600;letter-spacing:.5px;text-transform:uppercase;color:var(--white);background:var(--cyan);padding:17px 40px}
.btn--dark{background:var(--navy)}

/* header */
.site-header{position:absolute;top:0;left:0;width:1200px;height:72px;z-index:5}
.site-header nav{position:absolute;top:0;height:40px;display:flex;gap:30px;align-items:center;font-size:13px;font-weight:500;color:var(--white);text-transform:uppercase}
.nav-left{left:84px}
.nav-right{right:84px}
.cart-count{display:inline-flex;width:22px;height:22px;border-radius:50%;background:var(--cyan);align-items:center;justify-content:center;font-size:11px;margin-left:6px}
.logo-tab{position:absolute;left:450px;top:0;width:300px;height:130px}
.logo-tab svg{position:absolute;inset:0}
.brand{position:absolute;left:0;right:0;top:30px;text-align:center;font-weight:700;font-size:22px;line-height:1.15;color:var(--blue);text-transform:uppercase;letter-spacing:1px}

/* hero */
.hero{position:absolute;top:0;left:0;width:1200px;height:720px;background:linear-gradient(180deg,#2a3a4e 0%,#4f6c88 40%,#8fa9bf 75%,#5b7288 100%);text-align:center;color:var(--white)}
.hero::after{content:"";position:absolute;inset:0;background:rgba(20,30,45,.35)}
.hero-inner{position:relative;z-index:2;padding-top:345px}
.hero h1{font-size:44px;font-weight:700;letter-spacing:1px;text-transform:uppercase}
.hero p{width:640px;margin:18px auto 34px;font-size:14px;line-height:1.6;opacity:.9}

/* about */
.about{position:absolute;top:720px;left:0;width:1200px;height:672px;background:var(--white)}
.about-photo{position:absolute;left:0;top:0;width:410px;height:672px;background:linear-gradient(160deg,#3b7fc0,#6fb6e6 55%,#2a5f9a)}
.about-figure{position:absolute;left:200px;top:120px;width:300px;height:450px;background:linear-gradient(180deg,#d8dde2,#b8262f 60%,#1c2430);border-radius:40px;opacity:.9}
.about-text{position:absolute;left:670px;top:170px;width:430px}
.eyebrow{display:flex;align-items:center;gap:14px;font-size:11px;font-weight:600;color:var(--cyan);text-transform:uppercase;letter-spacing:1px}
.eyebrow::before{content:"";width:60px;height:2px;background:var(--cyan)}
.about h2{margin:14px 0 20px;font-size:38px;font-weight:600;line-height:1.15;text-transform:uppercase;color:var(--ink)}
.about p{font-size:14px;line-height:1.7;color:var(--text);margin-bottom:30px}

/* programs */
.program{position:absolute;left:0;width:1200px;height:448px}
.program-text{position:absolute;top:0;width:600px;height:448px;background:var(--pale);padding:0 84px;display:flex;flex-direction:column;justify-content:center}
.program-photo{position:absolute;top:0;width:600px;height:448px}
.program h3{font-size:38px;font-weight:600;line-height:1.15;text-transform:uppercase;color:var(--ink)}
.program p{font-size:13px;line-height:1.7;color:var(--text);margin:14px 0 28px;width:400px}
.program .btn{align-self:flex-start;padding:15px 44px}
.spring{top:1392px}
.spring .program-text{left:0}
.spring .program-photo{left:600px;background:linear-gradient(135deg,#0e2a4a,#3f78a8 55%,#152d47)}
.summer{top:1840px}
.summer .program-photo{left:0;background:linear-gradient(180deg,#6c8e57,#3f6a3a 50%,#8fa66a)}
.summer .program-text{left:600px;background:var(--white)}
.winter{top:2288px}
.winter .program-text{left:0}
.winter .program-photo{left:600px;background:linear-gradient(135deg,#e8eef4,#c9d6e2 50%,#b13b3b 85%)}

/* tournament */
.tournament{position:absolute;top:2736px;left:0;width:1200px;height:752px;text-align:center;background:var(--white)}
.tournament h2{margin-top:84px;font-size:38px;font-weight:600;text-transform:uppercase}
.tournament .intro{width:680px;margin:10px auto 0;font-size:13px;line-height:1.7;color:var(--text)}
.cards{position:absolute;top:228px;left:88px;display:flex;gap:16px}
.card{position:relative;width:336px;height:360px;text-align:left;color:var(--white);overflow:hidden}
.card-photo{position:absolute;inset:0}
.card:nth-child(1) .card-photo{background:linear-gradient(160deg,#2b3f57,#5d7894 60%,#1e2b3a)}
.card:nth-child(2) .card-photo{background:linear-gradient(160deg,#a06a45,#c9a37e 50%,#3e5068)}
.card:nth-child(3) .card-photo{background:linear-gradient(160deg,#3a4f66,#7e97ad 55%,#20303f)}
.card::after{content:"";position:absolute;inset:0;background:linear-gradient(180deg,transparent 45%,rgba(15,25,40,.8))}
.card-body{position:absolute;left:26px;right:26px;bottom:26px;z-index:2}
.date{display:inline-flex;align-items:center;gap:8px;background:var(--cyan);border-radius:3px;padding:6px 12px;font-size:10px;font-weight:600;text-transform:uppercase}
.date small{display:block;font-size:8px;font-weight:400}
.card h4{margin-top:12px;font-size:17px;font-weight:500;line-height:1.3;text-transform:uppercase}
.view-all{position:absolute;left:0;right:0;top:668px;font-size:12px;font-weight:600;text-transform:uppercase;display:flex;justify-content:center;align-items:center;gap:12px}

/* footer */
.site-footer{position:absolute;top:3488px;left:0;width:1200px;height:360px;background:var(--navy);color:var(--white);text-align:center}
.footer-nav{position:absolute;top:90px;display:flex;gap:34px;font-size:13px}
.footer-left{left:84px}
.footer-right{right:84px}
.footer-brand{position:absolute;left:0;right:0;top:70px;font-weight:700;font-size:22px;line-height:1.15;color:var(--cyan);text-transform:uppercase;letter-spacing:1px}
.footer-rule{position:absolute;left:84px;right:84px;top:180px;height:1px;background:rgba(255,255,255,.12)}
.copyright{position:absolute;left:0;right:0;top:200px;font-size:12px;opacity:.75}
.social{position:absolute;left:0;right:0;top:240px;display:flex;justify-content:center;gap:14px}
.social span{width:34px;height:34px;border:1px solid rgba(255,255,255,.7)}
</style>
</head>
<body>

<header class="site-header">
  <nav class="nav-left"><a href="#">Home</a><a href="#">Spring Program</a><a href="#">Summer Program</a></nav>
  <div class="logo-tab">
    <svg width="300" height="130" viewBox="0 0 300 130"><polygon points="0,0 300,0 270,118 30,118" fill="#ffffff"/></svg>
    <div class="brand">Braveridge<br>Hockey</div>
  </div>
  <nav class="nav-right"><a href="#">Winter</a><a href="#">Tournament</a><a href="#">Cart<span class="cart-count">0</span></a></nav>
</header>

<section class="hero" role="img" aria-label="Youth hockey players skating on an indoor rink">
  <div class="hero-inner">
    <h1>Braveridge Hockey Development</h1>
    <p>Year-round training for young players who want to skate faster, shoot harder and think smarter on the ice, led by coaches who love the game and teach it well.</p>
    <a class="btn" href="#">Hockey Development Program</a>
  </div>
</section>

<section class="about">
  <div class="about-photo" role="img" aria-label="Blue arena backdrop"></div>
  <div class="about-figure" role="img" aria-label="Hockey player in white and red gear holding a stick"></div>
  <div class="about-text">
    <div class="eyebrow">About us</div>
    <h2>Welcome<br>to Braveridge Hockey Development</h2>
    <p>Our programs give youth athletes the skills, confidence and habits to grow in every season. Small groups and focused drills mean each skater gets real attention. We work on skating, puck handling, passing and game sense, and we build strong teammates along the way. Families trust us to help their players improve and enjoy the sport.</p>
    <a class="btn btn--dark" href="#">Learn more</a>
  </div>
</section>

<section class="program spring">
  <div class="program-text">
    <h3>Spirng<br>Program</h3>
    <p>Spring sessions sharpen edges and skills after the season ends. Players work in small groups on skating power, stickhandling and shooting in a fun setting.</p>
    <a class="btn" href="#">Details</a>
  </div>
  <div class="program-photo" role="img" aria-label="Skater chasing a flying puck on dark ice"></div>
</section>

<section class="program summer">
  <div class="program-photo" role="img" aria-label="Young players running drills on a summer field"></div>
  <div class="program-text">
    <h3>Summer<br>Program</h3>
    <p>Summer camp mixes dryland training with ice time. Athletes build speed, strength and agility, then put it to work in games and team challenges.</p>
    <a class="btn" href="#">Details</a>
  </div>
</section>

<section class="program winter">
  <div class="program-text">
    <h3>Winter<br>Program</h3>
    <p>Winter training runs alongside the season. Weekly ice sessions focus on positioning, game reads and skill work that carries straight into games.</p>
    <a class="btn" href="#">Details</a>
  </div>
  <div class="program-photo" role="img" aria-label="Players in red and white battling in front of a goalie"></div>
</section>

<section class="tournament">
  <h2>Tournament</h2>
  <p class="intro">Put your skills to the test against teams from across the region. Our tournaments give every player meaningful ice time and a great weekend of hockey.</p>
  <div class="cards">
    <article class="card">
      <div class="card-photo" role="img" aria-label="Players battling for the puck"></div>
      <div class="card-body">
        <span class="date">&#9633;<span><small>Saturday</small>15 August 2022</span></span>
        <h4>Lorem ipsum dolor sit amet, adipiscing elit.</h4>
      </div>
    </article>
    <article class="card">
      <div class="card-photo" role="img" aria-label="Indoor game in a gym"></div>
      <div class="card-body">
        <span class="date">&#9633;<span><small>Saturday</small>15 August 2022</span></span>
        <h4>Lorem ipsum dolor sit amet, adipiscing elit.</h4>
      </div>
    </article>
    <article class="card">
      <div class="card-photo" role="img" aria-label="Skaters racing on an arena rink"></div>
      <div class="card-body">
        <span class="date">&#9633;<span><small>Saturday</small>15 August 2022</span></span>
        <h4>Lorem ipsum dolor sit amet, adipiscing elit.</h4>
      </div>
    </article>
  </div>
  <a class="view-all" href="#">View all tournaments
    <svg width="26" height="10" viewBox="0 0 26 10"><path d="M0 5H24M19 1L24 5L19 9" fill="none" stroke="#243244" stroke-width="1.5"/></svg>
  </a>
</section>

<footer class="site-footer">
  <nav class="footer-nav footer-left"><a href="#">Home</a><a href="#">Spring Program</a><a href="#">Summer Program</a></nav>
  <div class="footer-brand">Braveridge<br>Hockey</div>
  <nav class="footer-nav footer-right"><a href="#">Winter</a><a href="#">Tournament</a><a href="#">Contact</a></nav>
  <div class="footer-rule"></div>
  <p class="copyright">©2022 Braveridge Hockey Development - Do not copy. All rights reserved.</p>
  <div class="social"><span></span><span></span><span></span></div>
</footer>

</body>
</html>
```